Morvetta Designs - Online Shoe Shop

Morvetta is an online shoes and bags shop. We sell Imported Genuine Leather shoes and bags our market is LSM 8-10. We mainly sell women shoes and bags and we will also be introducing men’s shoes and belts.
I would like a website design and development that is responsive, clean, elegant and easy to use. Where customers can make a purchase online.
Have CATEGORIES in SHOE STYLE (i.e. Heels, Sandals, Pumps, Mules, Boots, Sneaker, Flats, etc) and PRICE RANGE should be in South African Rands currency, COLOUR, SIZE.
For shoe images we should be able to add videos as well.
Header and Footer Menu should have the basic menu list. Header Menu (New Arrivals, Preorder, Women’s Collection, Men’s Collection, Summer 2020 Collection, Winter 2020 Collection, Bags, Accessories, Sale, etc
Auto display when the item is SOLD OUT. Add an option for a user to get notification on when the item is back in stock.
Icons to show when shoes are on sale and Show was and now price.
Users to be able to review and rate the items.
Discount codes for new email subscribers.
Consumers should be able to pay using different options, Credit card, QuidLane, EFT, etc
Add an option for discount coupons at checkout.
After placing and order they should receive an email with order receipt.
Site should have a shipping and tracking option. International shipping such as KRT and BOLTAIR. For local shipping in South Africa please add Quickpath Couriers and Zenobi Couriers.
Backend: Backend should be easy to add more categories, items and changing header banners, adding sale alerts. To get notification when the stock is low and sold out. Get notification when an order is placed online so to prepare packing for shipping.
Can we make sure that the SEO is in place and bare in mind all searchy rules to avoid being penalized.
Target Market(s)
Women from age 25-65
LSM 8-10
Entire South Africa and neighboring countries
Industry/Entity Type
Shoe Store
Coding
Coded - Design and coding required
Number of Pages Required
5+ page
Requirements
Must have
- Responsive
Clean
Modern
Shopping cart
Shipping options integration
Newsletter subscription
Social media icons
Nice to have
- The business colors are Gold and White or Gold and Black

```html
<!DOCTYPE html>
<html lang="en">
<head>
<meta charset="utf-8">
<title>Morvetta – Women's Shoes</title>
<link href="https://fonts.googleapis.com/css2?family=Roboto:wght@300;400;500;700&family=Raleway:wght@300;400&display=swap" rel="stylesheet">
<style>
:root{
  --gold:#f2b705;
  --gold-dark:#d9a300;
  --price:#eb9a0c;
  --black:#1a1a1a;
  --nav:#333333;
  --bar:#454545;
  --text:#333;
  --muted:#777;
  --line:#dddddd;
  --soft:#f1f1f1;
  --heart:#e8141c;
  --footer:#232323;
}
*{box-sizing:border-box;margin:0;padding:0}
html,body{width:1200px;height:3343px;overflow:hidden}
body{font-family:"Roboto",sans-serif;color:var(--text);background:#fff;position:relative;font-size:12px}
a{color:inherit;text-decoration:none}
.abs{position:absolute}

/* top bar */
.topbar{position:absolute;left:0;top:0;width:1200px;height:54px;background:var(--black)}
.topbar .socials{position:absolute;left:93px;top:15px;display:flex;gap:4px}
.topbar .socials span{width:22px;height:22px;border-radius:50%;background:#fff;display:block}
.topbar .deals{position:absolute;left:480px;top:12px;width:117px;height:29px;background:var(--gold);color:#fff;font-size:10px;font-weight:500;display:flex;align-items:center;justify-content:center;text-transform:uppercase}
.topbar .wholesale{position:absolute;left:601px;top:12px;width:116px;height:29px;background:#fff;color:#222;font-size:10px;display:flex;align-items:center;justify-content:center;text-transform:uppercase}
.topbar .wholesale b{color:var(--gold);font-weight:400;margin-left:3px}
.topbar .tools{position:absolute;left:1023px;top:14px;display:flex;gap:12px;align-items:center}
.topbar .search{width:26px;height:26px;border-radius:50%;background:var(--gold);display:flex;align-items:center;justify-content:center}

/* nav */
.mainnav{position:absolute;left:0;top:54px;width:1200px;height:50px;background:var(--nav)}
.mainnav ul{list-style:none;display:flex;position:absolute;left:93px;top:0;height:50px;align-items:center;gap:31px;color:#fff;font-size:12px}
.mainnav .locale{position:absolute;left:1024px;top:0;width:82px;height:50px;background:#262626;display:flex;align-items:center;justify-content:center;gap:14px;color:#fff;font-size:11px}
.mainnav .locale .cur{color:var(--gold)}

/* header */
.header{position:absolute;left:0;top:104px;width:1200px;height:90px;border-bottom:1px solid #eee}
.logo{position:absolute;left:93px;top:6px;display:flex;flex-direction:column;align-items:center;width:90px}
.logo .mark{width:40px;height:40px;background:var(--black)}
.logo .name{font-family:"Roboto",sans-serif;font-weight:700;font-size:22px;color:var(--black);margin-top:4px}
.welcome{position:absolute;left:787px;top:18px;font-size:11px;color:#222}
.login{position:absolute;left:855px;top:39px;width:78px;height:27px;background:var(--gold);color:#fff;font-size:10px;display:flex;align-items:center;justify-content:center;gap:4px}
.cart{position:absolute;left:943px;top:21px;width:163px;height:45px;border:1px solid var(--line);display:flex}
.cart .icon{width:46px;border-right:1px solid var(--line);display:flex;align-items:center;justify-content:center}
.cart .info{padding:8px 8px;font-size:10px;color:#555;line-height:14px}
.cart .info small{color:#999;font-size:9px}
.cart .chev{position:absolute;right:6px;top:17px;font-size:9px;color:#888}

.breadcrumb{position:absolute;left:93px;top:206px;font-size:9px;color:#999}
.breadcrumb b{color:#333;font-weight:400}

/* sidebar */
.sidebar{position:absolute;left:93px;top:246px;width:213px}
.side-head{background:var(--bar);color:#fff;font-weight:500;font-size:14px;height:30px;line-height:30px;padding-left:15px;text-transform:uppercase}
.side-list{list-style:none;font-size:11px;color:#555;text-transform:uppercase}
.cats li{height:31px;line-height:31px;padding-left:12px}
.cats li.active{background:var(--soft);margin-top:10px;height:30px;position:relative}
.cats li.active::after{content:"›";position:absolute;right:18px;color:#444}
.styles{margin:14px 0 14px}
.styles li{height:31px;line-height:18px}
.price-slider{position:relative;height:50px;margin-top:8px}
.price-slider .track{position:absolute;left:5px;right:5px;top:12px;height:2px;background:#3c78d8}
.price-slider .knob{position:absolute;top:7px;width:11px;height:11px;border-radius:50%;background:var(--gold)}
.price-slider .ticks{position:absolute;left:20px;right:20px;top:27px;display:flex;justify-content:space-between}
.price-slider .ticks i{width:2px;height:2px;background:#777;display:block}
.price-range{display:flex;align-items:center;height:25px;margin-bottom:22px;font-size:11px;color:#555}
.select{height:25px;border:1px solid #bbb;display:flex;align-items:center;justify-content:space-between;padding:0 8px;font-size:10px}
.select::after{content:"";border:4px solid transparent;border-top:5px solid #222;margin-top:4px}
.sizes{margin:13px 0 16px}
.sizes li,.colors li{display:flex;align-items:center;gap:10px;text-transform:none}
.sizes li{height:26px}
.box{width:10px;height:10px;border:1px solid #ccc;display:block}
.colors{margin-top:10px}
.colors li{height:34px;font-size:11px;text-transform:uppercase}
.swatch{width:28px;height:28px;border-radius:50%;display:block;margin-left:-2px}

/* listing */
.listing{position:absolute;left:348px;top:244px;width:758px}
.listing .count{font-size:11px;color:#333}
.listing .count span{color:#888}
.sortby{display:flex;gap:37px;font-size:11px;color:#333;margin-top:10px;height:24px}
.sortby .on{color:#222;position:relative}
.sortby .on::after{content:"";position:absolute;left:0;right:0;bottom:-6px;height:2px;background:#3c78d8}
.grid{position:absolute;left:348px;top:297px;width:759px;display:grid;grid-template-columns:repeat(3,243px);column-gap:15px;row-gap:19px}
.card{height:284px;border:1px solid var(--line);position:relative}
.card .photo{position:absolute;left:16px;right:16px;top:12px;height:150px}
.card .fav{position:absolute;right:9px;top:9px}
.card h3{position:absolute;left:13px;top:167px;font-family:"Raleway",sans-serif;font-weight:400;font-size:16px;color:#333}
.card .price{position:absolute;left:13px;top:189px;font-size:12px;color:var(--price)}
.card .stars{position:absolute;left:13px;top:209px;font-size:9px;color:var(--gold);letter-spacing:2px}
.card .add{position:absolute;left:14px;top:235px;width:116px;height:29px;background:var(--gold);color:#fff;font-size:10px;font-weight:500;display:flex;align-items:center;justify-content:center}
.card .details{position:absolute;left:147px;top:244px;font-size:11px;color:#333}

.pager{position:absolute;left:348px;top:2114px;width:759px;border-top:2px solid #e5e5e5;padding-top:17px;height:40px}
.pager .page{position:absolute;left:0;top:25px;font-size:11px}
.pager ol{position:absolute;left:280px;top:18px;list-style:none;display:flex;gap:12px;align-items:center;font-size:11px}
.pager ol li{width:20px;text-align:center}
.pager ol li.now{width:25px;height:25px;border-radius:50%;background:#f26522;color:#fff;line-height:25px}
.pager ol li.next{color:var(--price);width:auto;margin-left:6px}
.feedback{position:absolute;left:348px;top:2174px;width:759px;height:40px;background:#f3f3f3;display:flex;align-items:center;padding-left:14px;font-size:12px}
.feedback .btn{width:62px;height:25px;border:1px solid #888;background:#fff;display:flex;align-items:center;justify-content:center;font-size:11px}
.feedback .yes{margin-left:28px}
.feedback .no{margin-left:6px}

/* reviews */
.reviews{position:absolute;left:93px;top:2272px;width:1014px}
.reviews h2{font-size:25px;font-weight:500;color:#222}
.review{position:absolute;left:0;width:1014px;height:143px;border-bottom:1px solid #e5e5e5}
.review .thumb{position:absolute;left:0;top:8px;width:115px;height:75px}
.review .meta{position:absolute;left:130px;top:0;font-size:12px;line-height:19px;color:#333}
.review .meta b{font-weight:500}
.review .meta .rate{font-size:11px}
.review .meta .rate i{color:var(--gold);font-style:normal}
.helpful{position:absolute;top:0;width:210px;font-size:9px;color:#777;line-height:14.5px}
.helpful .tag{color:#888;font-size:9px}
.helpful .title{font-size:12px;color:#222;font-weight:500;display:flex;align-items:center;gap:6px;margin:2px 0 2px}
.helpful .score{background:#2a6ab3;color:#fff;font-size:9px;padding:0 4px;height:13px;line-height:13px}

/* footer */
.footer{position:absolute;left:0;top:2802px;width:1200px;height:541px;background:var(--footer);color:#bbb}
.fcol{position:absolute;top:55px}
.fcol h4{color:#fff;font-size:18px;font-weight:500;text-transform:uppercase;margin-bottom:11px}
.fcol ul{list-style:none;font-size:12px;line-height:27px;color:#aaa}
.newsletter input,.newsletter button{display:block;width:221px;height:29px;border:none;margin-bottom:5px;font-family:inherit;font-size:10px;padding-left:8px}
.newsletter input{background:#fff;color:#555}
.newsletter button{background:var(--gold);color:#fff;font-weight:500;padding:0;margin-top:0}
.social li{display:flex;align-items:center;gap:10px;line-height:30px;font-size:12px}
.social li span{width:20px;height:20px;border-radius:50%;background:#fff;display:block}
.promise{position:absolute;top:292px;display:flex;gap:24px}
.promise .circ{width:57px;height:57px;border-radius:50%;background:var(--gold);display:flex;align-items:center;justify-content:center}
.promise h5{color:var(--gold);font-size:15px;font-weight:500;margin-top:8px}
.promise p{font-size:11px;color:#aaa;line-height:14px;width:190px}
.footline{position:absolute;left:93px;top:367px;width:1014px;height:1px;background:#444}
.secure{position:absolute;left:0;width:1200px;top:390px;text-align:center;color:#fff}
.secure small{font-size:8px;display:block}
.secure .brand{font-size:17px;font-weight:700;display:block;margin-top:2px}
.secure .cards{display:flex;gap:3px;justify-content:center;margin-top:4px}
.secure .cards span{width:26px;height:16px;display:block}
.copy{position:absolute;left:0;width:1200px;top:475px;text-align:center;font-size:12px;color:#aaa}
.copy b{color:var(--gold);font-weight:400}
</style>
</head>
<body>

<header>
  <div class="topbar">
    <div class="socials" aria-label="Social links">
      <span></span><span></span><span></span><span></span><span></span>
    </div>
    <a class="deals">Latest Deals</a>
    <a class="wholesale">Wholesale <b>Login</b></a>
    <div class="tools">
      <span class="search"><svg width="12" height="12" viewBox="0 0 12 12"><circle cx="5" cy="5" r="3.5" fill="none" stroke="#222" stroke-width="1.6"/><line x1="7.6" y1="7.6" x2="11" y2="11" stroke="#222" stroke-width="1.8"/></svg></span>
      <svg width="16" height="16" viewBox="0 0 16 16"><circle cx="8" cy="5" r="4" fill="#fff"/><path d="M1 16c0-5 3-7 7-7s7 2 7 7z" fill="#fff"/></svg>
      <svg width="17" height="15" viewBox="0 0 24 21"><path d="M12 21 2 11A6 6 0 0 1 12 3a6 6 0 0 1 10 8z" fill="#fff"/></svg>
    </div>
  </div>

  <nav class="mainnav">
    <ul>
      <li>New Arrivals</li><li>Preorder</li><li>Women's Collection</li><li>Men's Collection</li>
      <li>Summer 2020 Collection</li><li>Winter 2020 Collection</li><li>Bags</li><li>Accessories</li><li>Sale</li>
    </ul>
    <div class="locale"><span>En ⌄</span><span class="cur">$ ⌄</span></div>
  </nav>

  <div class="header">
    <div class="logo"><span class="mark"></span><span class="name">Morvetta</span></div>
    <p class="welcome">Welcome To our online store!</p>
    <a class="login"><svg width="11" height="11" viewBox="0 0 12 12"><circle cx="6" cy="6" r="5" fill="none" stroke="#fff" stroke-width="1.3"/><path d="M4 6h4M6.5 4.5 8 6 6.5 7.5" stroke="#fff" fill="none" stroke-width="1.2"/></svg>Log In</a>
    <div class="cart">
      <span class="icon"><svg width="20" height="17" viewBox="0 0 20 17"><path d="M1 6h18l-2 10H3z" fill="#222"/><path d="M5 6 9 1M15 6 11 1" stroke="#222" stroke-width="1.5" fill="none"/></svg></span>
      <div class="info">My Cart:<br><small>0 item(s)-$0.00</small></div>
      <span class="chev">⌄</span>
    </div>
  </div>
</header>

<p class="breadcrumb">HOME &gt; <b>WOMEN'S SHOES</b></p>

<aside class="sidebar">
  <div class="side-head">Categories</div>
  <ul class="side-list cats">
    <li class="active">Women Shoes</li><li>Women Bags</li><li>Men's Shoes</li><li>Men's Belts</li>
  </ul>
  <div class="side-head" style="margin-top:12px">Shoe Style</div>
  <ul class="side-list styles">
    <li>Heels</li><li>Sandals</li><li>Pumps</li><li>Mules</li><li>Boots</li><li>Sneaker</li><li>Flats</li>
  </ul>
  <div class="side-head" style="margin-top:-12px">Price</div>
  <div class="price-slider">
    <span class="track"></span>
    <span class="knob" style="left:0"></span><span class="knob" style="right:0"></span>
    <span class="ticks"><i></i><i></i><i></i><i></i><i></i><i></i><i></i></span>
  </div>
  <div class="price-range">
    <span class="select" style="width:83px">Min</span>
    <span style="margin:0 26px 0 27px">to</span>
    <span class="select" style="width:82px">R 3000+</span>
  </div>
  <div class="side-head">Size</div>
  <ul class="side-list sizes">
    <li><span class="box"></span>2</li><li><span class="box"></span>2.5</li><li><span class="box"></span>3</li><li><span class="box"></span>5</li><li><span class="box"></span>6</li>
  </ul>
  <div class="side-head">Color</div>
  <ul class="side-list colors">
    <li><span class="box"></span><span class="swatch" style="background:#e6236e"></span>Beige</li>
    <li><span class="box"></span><span class="swatch" style="background:#000"></span>Black</li>
    <li><span class="box"></span><span class="swatch" style="background:#1e7be0"></span>Blue</li>
    <li><span class="box"></span><span class="swatch" style="background:#efc30e"></span>Gold</li>
    <li><span class="box"></span><span class="swatch" style="background:#7f1d1d"></span>Brown</li>
  </ul>
</aside>

<section class="listing">
  <p class="count">Women's Shoes <span>(Showing 1 – 40 products of 80,292 products)</span></p>
  <div class="sortby"><span>Sort By</span><span class="on">Popularity</span><span>Price -- Low to High</span><span>Price -- High to Low</span><span>Newest First</span></div>
</section>

<main class="grid">
  <article class="card"><div class="photo" role="img" aria-label="Pink mesh sneakers" style="background:radial-gradient(ellipse at 45% 55%,#e0488e 0%,#f3a8c8 45%,#fff 72%)"></div><svg class="fav" width="20" height="18" viewBox="0 0 24 21"><path d="M12 21 2 11A6 6 0 0 1 12 3a6 6 0 0 1 10 8z" fill="#ddd"/></svg><h3>Eiusmod Tempor</h3><p class="price">R 583.95</p><p class="stars">★★★★★</p><a class="add">ADD TO CART</a><a class="details">DETAILS</a></article>
  <article class="card"><div class="photo" role="img" aria-label="Red suede pump heels" style="background:radial-gradient(ellipse at 50% 55%,#e8141c 0%,#f5868a 42%,#fff 70%)"></div><svg class="fav" width="20" height="18" viewBox="0 0 24 21"><path d="M12 21 2 11A6 6 0 0 1 12 3a6 6 0 0 1 10 8z" fill="var(--heart)"/></svg><h3>Eiusmod Tempor</h3><p class="price">R 583.95</p><p class="stars">★★★★★</p><a class="add">ADD TO CART</a><a class="details">DETAILS</a></article>
  <article class="card"><div class="photo" role="img" aria-label="Plum leather loafers" style="background:radial-gradient(ellipse at 50% 60%,#5a2339 0%,#a8788a 35%,#fff 62%)"></div><svg class="fav" width="20" height="18" viewBox="0 0 24 21"><path d="M12 21 2 11A6 6 0 0 1 12 3a6 6 0 0 1 10 8z" fill="#ddd"/></svg><h3>Eiusmod Tempor</h3><p class="price">R 583.95</p><p class="stars">★★★★★</p><a class="add">ADD TO CART</a><a class="details">DETAILS</a></article>

  <article class="card"><div class="photo" role="img" aria-label="Mustard heels with patterned block heel" style="background:radial-gradient(ellipse at 50% 55%,#e6a416 0%,#f3d17e 42%,#fff 70%)"></div><svg class="fav" width="20" height="18" viewBox="0 0 24 21"><path d="M12 21 2 11A6 6 0 0 1 12 3a6 6 0 0 1 10 8z" fill="#ddd"/></svg><h3>Eiusmod Tempor</h3><p class="price">R 583.95</p><p class="stars">★★★★★</p><a class="add">ADD TO CART</a><a class="details">DETAILS</a></article>
  <article class="card"><div class="photo" role="img" aria-label="Red canvas sneakers" style="background:radial-gradient(ellipse at 50% 58%,#b5243f 0%,#df98a6 40%,#fff 68%)"></div><svg class="fav" width="20" height="18" viewBox="0 0 24 21"><path d="M12 21 2 11A6 6 0 0 1 12 3a6 6 0 0 1 10 8z" fill="#ddd"/></svg><h3>Eiusmod Tempor</h3><p class="price">R 583.95</p><p class="stars">★★★★★</p><a class="add">ADD TO CART</a><a class="details">DETAILS</a></article>
  <article class="card"><div class="photo" role="img" aria-label="Brown ankle heels" style="background:radial-gradient(ellipse at 50% 50%,#3f2c26 0%,#a4928b 40%,#fff 68%)"></div><svg class="fav" width="20" height="18" viewBox="0 0 24 21"><path d="M12 21 2 11A6 6 0 0 1 12 3a6 6 0 0 1 10 8z" fill="#ddd"/></svg><h3>Eiusmod Tempor</h3><p class="price">R 583.95</p><p class="stars">★★★★★</p><a class="add">ADD TO CART</a><a class="details">DETAILS</a></article>

  <article class="card"><div class="photo" role="img" aria-label="Black ballet flats with bows" style="background:radial-gradient(ellipse at 50% 50%,#111 0%,#8c8c8c 40%,#fff 68%)"></div><svg class="fav" width="20" height="18" viewBox="0 0 24 21"><path d="M12 21 2 11A6 6 0 0 1 12 3a6 6 0 0 1 10 8z" fill="var(--heart)"/></svg><h3>Eiusmod Tempor</h3><p class="price">R 583.95</p><p class="stars">★★★★★</p><a class="add">ADD TO CART</a><a class="details">DETAILS</a></article>
  <article class="card"><div class="photo" role="img" aria-label="Beige ballet flats" style="background:radial-gradient(ellipse at 50% 50%,#e5c08f 0%,#f2dcc4 42%,#fff 70%)"></div><svg class="fav" width="20" height="18" viewBox="0 0 24 21"><path d="M12 21 2 11A6 6 0 0 1 12 3a6 6 0 0 1 10 8z" fill="#ddd"/></svg><h3>Eiusmod Tempor</h3><p class="price">R 583.95</p><p class="stars">★★★★★</p><a class="add">ADD TO CART</a><a class="details">DETAILS</a></article>
  <article class="card"><div class="photo" role="img" aria-label="Brown leather flats" style="background:radial-gradient(ellipse at 50% 50%,#4b3030 0%,#a8908c 38%,#fff 66%)"></div><svg class="fav" width="20" height="18" viewBox="0 0 24 21"><path d="M12 21 2 11A6 6 0 0 1 12 3a6 6 0 0 1 10 8z" fill="#ddd"/></svg><h3>Eiusmod Tempor</h3><p class="price">R 583.95</p><p class="stars">★★★★★</p><a class="add">ADD TO CART</a><a class="details">DETAILS</a></article>

  <article class="card"><div class="photo" role="img" aria-label="Pink mesh sneakers" style="background:radial-gradient(ellipse at 45% 55%,#e0488e 0%,#f3a8c8 45%,#fff 72%)"></div><svg class="fav" width="20" height="18" viewBox="0 0 24 21"><path d="M12 21 2 11A6 6 0 0 1 12 3a6 6 0 0 1 10 8z" fill="#ddd"/></svg><h3>Eiusmod Tempor</h3><p class="price">R 583.95</p><p class="stars">★★★★★</p><a class="add">ADD TO CART</a><a class="details">DETAILS</a></article>
  <article class="card"><div class="photo" role="img" aria-label="Royal blue suede heel" style="background:radial-gradient(ellipse at 50% 55%,#1c3f9e 0%,#8ea3da 40%,#fff 68%)"></div><svg class="fav" width="20" height="18" viewBox="0 0 24 21"><path d="M12 21 2 11A6 6 0 0 1 12 3a6 6 0 0 1 10 8z" fill="var(--heart)"/></svg><h3>Eiusmod Tempor</h3><p class="price">R 583.95</p><p class="stars">★★★★★</p><a class="add">ADD TO CART</a><a class="details">DETAILS</a></article>
  <article class="card"><div class="photo" role="img" aria-label="Plum leather loafers" style="background:radial-gradient(ellipse at 50% 60%,#5a2339 0%,#a8788a 35%,#fff 62%)"></div><svg class="fav" width="20" height="18" viewBox="0 0 24 21"><path d="M12 21 2 11A6 6 0 0 1 12 3a6 6 0 0 1 10 8z" fill="#ddd"/></svg><h3>Eiusmod Tempor</h3><p class="price">R 583.95</p><p class="stars">★★★★★</p><a class="add">ADD TO CART</a><a class="details">DETAILS</a></article>

  <article class="card"><div class="photo" role="img" aria-label="Black and white slide sandals" style="background:radial-gradient(ellipse at 50% 55%,#222 0%,#b3b3b3 40%,#fff 68%)"></div><svg class="fav" width="20" height="18" viewBox="0 0 24 21"><path d="M12 21 2 11A6 6 0 0 1 12 3a6 6 0 0 1 10 8z" fill="#ddd"/></svg><h3>Eiusmod Tempor</h3><p class="price">R 583.95</p><p class="stars">★★★★★</p><a class="add">ADD TO CART</a><a class="details">DETAILS</a></article>
  <article class="card"><div class="photo" role="img" aria-label="Mustard heels with patterned block heel" style="background:radial-gradient(ellipse at 50% 55%,#e6a416 0%,#f3d17e 42%,#fff 70%)"></div><svg class="fav" width="20" height="18" viewBox="0 0 24 21"><path d="M12 21 2 11A6 6 0 0 1 12 3a6 6 0 0 1 10 8z" fill="#ddd"/></svg><h3>Eiusmod Tempor</h3><p class="price">R 583.95</p><p class="stars">★★★★★</p><a class="add">ADD TO CART</a><a class="details">DETAILS</a></article>
  <article class="card"><div class="photo" role="img" aria-label="Teal knit slip-on sneakers" style="background:radial-gradient(ellipse at 50% 55%,#2f7c83 0%,#9cc4c6 40%,#fff 68%)"></div><svg class="fav" width="20" height="18" viewBox="0 0 24 21"><path d="M12 21 2 11A6 6 0 0 1 12 3a6 6 0 0 1 10 8z" fill="#ddd"/></svg><h3>Eiusmod Tempor</h3><p class="price">R 583.95</p><p class="stars">★★★★★</p><a class="add">ADD TO CART</a><a class="details">DETAILS</a></article>

  <article class="card"><div class="photo" role="img" aria-label="Black ballet flats with bows" style="background:radial-gradient(ellipse at 50% 50%,#111 0%,#8c8c8c 40%,#fff 68%)"></div><svg class="fav" width="20" height="18" viewBox="0 0 24 21"><path d="M12 21 2 11A6 6 0 0 1 12 3a6 6 0 0 1 10 8z" fill="var(--heart)"/></svg><h3>Eiusmod Tempor</h3><p class="price">R 583.95</p><p class="stars">★★★★★</p><a class="add">ADD TO CART</a><a class="details">DETAILS</a></article>
  <article class="card"><div class="photo" role="img" aria-label="Beige ballet flats" style="background:radial-gradient(ellipse at 50% 50%,#e5c08f 0%,#f2dcc4 42%,#fff 70%)"></div><svg class="fav" width="20" height="18" viewBox="0 0 24 21"><path d="M12 21 2 11A6 6 0 0 1 12 3a6 6 0 0 1 10 8z" fill="#ddd"/></svg><h3>Eiusmod Tempor</h3><p class="price">R 583.95</p><p class="stars">★★★★★</p><a class="add">ADD TO CART</a><a class="details">DETAILS</a></article>
  <article class="card"><div class="photo" role="img" aria-label="Brown leather flats" style="background:radial-gradient(ellipse at 50% 50%,#4b3030 0%,#a8908c 38%,#fff 66%)"></div><svg class="fav" width="20" height="18" viewBox="0 0 24 21"><path d="M12 21 2 11A6 6 0 0 1 12 3a6 6 0 0 1 10 8z" fill="#ddd"/></svg><h3>Eiusmod Tempor</h3><p class="price">R 583.95</p><p class="stars">★★★★★</p><a class="add">ADD TO CART</a><a class="details">DETAILS</a></article>
</main>

<div class="pager">
  <span class="page">Page 1 of 15</span>
  <ol><li class="now">1</li><li>2</li><li>3</li><li>4</li><li>5</li><li class="next">Next</li></ol>
</div>
<div class="feedback">Did you find what you were looking for?<span class="btn yes">Yes</span><span class="btn no">No</span></div>

<section class="reviews">
  <h2>Reviews for Popular Women's Footwear</h2>

  <div class="review" style="top:82px">
    <div class="thumb" role="img" aria-label="Red canvas sneakers" style="background:radial-gradient(ellipse at 50% 55%,#b5243f 0%,#e2a3ae 40%,#fff 70%)"></div>
    <div class="meta"><b>1. Longwalk Perfect Stylish Gi...</b><br><span class="rate">4.22<i>★</i> Ratings&amp;393 Reviews</span><br>R 39860% off<br>Colour: Pink<br>Outer Material: Synthetic Leather</div>
    <div class="helpful" style="left:409px"><span class="tag">Most Helpful Review</span><p class="title"><span class="score">4.5 ★</span>Worth every penny</p>very nice product i am satisfied with this product but the print was rubbed easily and i got same product which i seen on the Morvetta</div>
    <div class="helpful" style="left:746px"><span class="tag">Most Helpful Review</span><p class="title"><span class="score">4.5 ★</span>Worth every penny</p>very nice product i am satisfied with this product but the print was rubbed easily and i got same product which i seen on the Morvetta</div>
  </div>

  <div class="review" style="top:225px">
    <div class="thumb" role="img" aria-label="Red suede pump heels" style="background:radial-gradient(ellipse at 50% 55%,#e8141c 0%,#f5868a 40%,#fff 70%)"></div>
    <div class="meta"><b>1. Longwalk Perfect Stylish Gi...</b><br><span class="rate">4.22<i>★</i> Ratings&amp;393 Reviews</span><br>R 39860% off<br>Colour: Pink<br>Outer Material: Synthetic Leather</div>
    <div class="helpful" style="left:409px"><span class="tag">Most Helpful Review</span><p class="title"><span class="score">4.5 ★</span>Worth every penny</p>very nice product i am satisfied with this product but the print was rubbed easily and i got same product which i seen on the Morvetta</div>
    <div class="helpful" style="left:746px"><span class="tag">Most Helpful Review</span><p class="title"><span class="score">4.5 ★</span>Worth every penny</p>very nice product i am satisfied with this product but the print was rubbed easily and i got same product which i seen on the Morvetta</div>
  </div>

  <div class="review" style="top:368px;border-bottom:none">
    <div class="thumb" role="img" aria-label="Teal knit slip-on sneakers" style="background:radial-gradient(ellipse at 50% 55%,#2f7c83 0%,#9cc4c6 40%,#fff 70%)"></div>
    <div class="meta"><b>1. Longwalk Perfect Stylish Gi...</b><br><span class="rate">4.22<i>★</i> Ratings&amp;393 Reviews</span><br>R 39860% off<br>Colour: Pink<br>Outer Material: Synthetic Leather</div>
    <div class="helpful" style="left:409px"><span class="tag">Most Helpful Review</span><p class="title"><span class="score">4.5 ★</span>Worth every penny</p>very nice product i am satisfied with this product but the print was rubbed easily and i got same product which i seen on the Morvetta</div>
    <div class="helpful" style="left:746px"><span class="tag">Most Helpful Review</span><p class="title"><span class="score">4.5 ★</span>Worth every penny</p>very nice product i am satisfied with this product but the print was rubbed easily and i got same product which i seen on the Morvetta</div>
  </div>
</section>

<footer class="footer">
  <div class="fcol" style="left:94px"><h4>About</h4><ul><li>Contact Us</li><li>About Us</li><li>Careers</li><li>Morvetta Stories</li><li>Press</li></ul></div>
  <div class="fcol" style="left:286px"><h4>Help</h4><ul><li>Payments</li><li>Shipping</li><li>Cancellation &amp; Returns</li><li>FAQ</li><li>Report Infringement</li></ul></div>
  <div class="fcol" style="left:521px"><h4>Policy</h4><ul><li>Return Policy</li><li>Terms Of Use</li><li>Security</li><li>Privacy</li><li>Sitemap</li></ul></div>
  <div class="fcol newsletter" style="left:713px"><h4>Newsletter</h4><input placeholder="Enter Name:"><input placeholder="Enter Email:"><button>SUBSCRIBE</button></div>
  <div class="fcol" style="left:1021px"><h4>Social</h4><ul class="social"><li><span></span>Friendlink</li><li><span></span>Chirpwave</li><li><span></span>Snapgallery</li><li><span></span>Vidstream</li><li><span></span>RSS</li></ul></div>

  <div class="promise" style="left:93px"><span class="circ"><svg width="28" height="20" viewBox="0 0 28 20"><rect x="1" y="3" width="16" height="11" fill="#222"/><path d="M17 6h6l4 4v4H17z" fill="#222"/><circle cx="7" cy="16" r="3" fill="#222"/><circle cx="21" cy="16" r="3" fill="#222"/></svg></span><div><h5>FREE SHIPPING</h5><p>Sed ut perspiciatis unde omnis iste natus error sit voluptatem</p></div></div>
  <div class="promise" style="left:468px"><span class="circ"><svg width="26" height="20" viewBox="0 0 26 20"><rect x="2" y="3" width="22" height="14" rx="2" fill="none" stroke="#222" stroke-width="2"/><rect x="2" y="7" width="22" height="3" fill="#222"/></svg></span><div><h5>SECURED PAYMENT</h5><p>Sed ut perspiciatis unde omnis iste natus error sit voluptatem</p></div></div>
  <div class="promise" style="left:838px"><span class="circ"><svg width="26" height="24" viewBox="0 0 26 24"><circle cx="15" cy="8" r="6" fill="none" stroke="#222" stroke-width="2"/><path d="M2 16h6l5 3h8v3H9l-7-2z" fill="#222"/></svg></span><div><h5>MONEY BACK GUARANTEE</h5><p>Sed ut perspiciatis unde omnis iste natus error sit voluptatem</p></div></div>

  <span class="footline"></span>
  <div class="secure">
    <small>Secure Payments by</small>
    <span class="brand">QuidLane</span>
    <div class="cards"><span style="background:#e4572e"></span><span style="background:#1a3b8f"></span><span style="background:#2e77bb"></span><span style="background:#ddd"></span></div>
  </div>
  <p class="copy">Copyright © 2020 <b>Morvetta</b>. All rights reserved.</p>
</footer>

</body>
</html>
```